Music producer seeks album cover!

Hi there designers. I need a design for my new album - the CD cover, CD itself and the album artwork for Tunevale and other streaming sites. This is my 'Salt and Thunder' album: it's about gender and sexuality, and not conforming to labels. Musically it combines the pink of disco with the purple of rock.

The front cover should only be visuals and 'rowan fedder' in all lower case with no capitals, and no album title, just a design in pink and purple please. I'd like to see something very simple, bold and iconic. For inspiration, how about jellyfish, squid, orca or zebra? All in pink and purple of course :-) Or how about the male and female parts of a flower, stamen and pistil?

For the back cover, I have quite a bit of text, attached as a word file.

The CD artwork and album artwork for streaming sites should be versions of the front cover. I will attach a template for the print-ready artwork . The streaming artwork needs to be a perfect square JPG or PNG, at least 4000 x 4000 pixels. It doesn't need the artist name.

```html
<!DOCTYPE html>
<html lang="en">
<head>
<meta charset="utf-8">
<title>rowan fedder – Salt and Thunder – back cover</title>
<link href="https://fonts.googleapis.com/css2?family=Archivo:wght@400;500;800&display=swap" rel="stylesheet">
<style>
  :root {
    --page: #121214;
    --ink: #f2eef6;
    --pink: #e0449a;
    --purple: #8a4ff0;
    --night: #150b2a;
    --deep: #2a1160;
    --glow-red: #8c1c3c;
    --glow-magenta: #b0309a;
  }
  * { margin: 0; padding: 0; box-sizing: border-box; }
  html, body { width: 1200px; height: 675px; overflow: hidden; background: var(--page); }
  body { font-family: "Archivo", Arial, sans-serif; color: var(--ink); }

  .back-cover {
    position: absolute; left: 200px; top: 17px;
    width: 800px; height: 640px; overflow: hidden;
  }
  .cover-artwork {
    position: absolute; inset: 0;
    background:
      radial-gradient(ellipse 200px 170px at 600px 250px, var(--glow-red), transparent 70%),
      radial-gradient(ellipse 260px 180px at 590px 360px, var(--glow-magenta), transparent 72%),
      radial-gradient(ellipse 320px 200px at 300px 460px, var(--deep), transparent 75%),
      linear-gradient(160deg, #0b0714 0%, var(--night) 55%, #1e0c3a 100%);
  }

  .tracklist {
    position: absolute; left: 40px; top: 48px;
    list-style: none; font-weight: 800; font-size: 26px; line-height: 27px; letter-spacing: -0.2px;
  }
  .pink { color: var(--pink); }
  .purple { color: var(--purple); }

  .production-notes {
    position: absolute; right: 30px; top: 24px; width: 130px;
    text-align: right; font-size: 12px; line-height: 13.5px;
  }

  .spaced-heading {
    position: absolute; left: 40px; font-size: 10px; letter-spacing: 9px;
  }
  .featuring-heading { top: 334px; }
  .mastering-credit { top: 572px; }

  .credits {
    position: absolute; left: 40px; right: 40px; top: 352px;
    font-size: 9.5px; line-height: 10.5px;
  }
  .credit-row { display: flex; justify-content: space-between; }

  .thanks {
    position: absolute; left: 40px; top: 590px; width: 560px;
    font-size: 8.5px; line-height: 10px;
  }
  .signature {
    position: absolute; right: 40px; top: 592px; text-align: right;
    font-size: 8.5px; line-height: 12px;
  }
  .website { color: var(--pink); font-weight: 500; font-size: 10px; }
</style>
</head>
<body>
<main class="back-cover">
  <div class="cover-artwork" role="img" aria-label="Photograph of a glowing jellyfish in pink, red and purple light against a dark background"></div>

  <ol class="tracklist">
    <li><span class="pink">marlow</span> harbourlight</li>
    <li><span class="purple">nettie</span> <span class="pink">swan</span></li>
    <li>drifter <span class="purple">glass</span> held my heart</li>
    <li>paris fell with the <span class="purple">rain?</span></li>
    <li>low tide</li>
    <li><span class="purple">wakarewa</span></li>
    <li>thornhill lane</li>
    <li><span class="pink">lovers</span> <span class="purple">letters</span></li>
    <li>quiet golden</li>
    <li><span class="pink">farewell</span></li>
  </ol>

  <p class="production-notes">rowan fedder’s <span class="pink">Salt and Thunder</span> album was written and produced by rowan fedder. spoken word on ‘marlow’ written by Simeon Coyle, string arrangement for ‘glass held my heart’ written by Nathan Pryce</p>

  <p class="spaced-heading featuring-heading">Featuring, in order of appearance:</p>

  <div class="credits">
    <div class="credit-row"><span>Simeon Coyle</span><span>spoken word, track 1</span></div>
    <div class="credit-row"><span>Felix Ortega (via Sessionfold)</span><span>organ on track 1, electric piano on track 8</span></div>
    <div class="credit-row"><span>rowan fedder</span><span>vocals, guitars, bass guitar, keyboards, sampler</span></div>
    <div class="credit-row"><span>Rafael Moss (via Sessionfold)</span><span>drums, tracks 1 and 7</span></div>
    <div class="credit-row"><span>Ines Delacroix-Voss</span><span>saxophones, tracks 1, 3, 5</span></div>
    <div class="credit-row"><span>Priya Sandhu (via Sessionfold)</span><span>vocals, tracks 2, 4, 5, 6, 7, 8, 10</span></div>
    <div class="credit-row"><span>Velvet Echo</span><span>organ, track 2</span></div>
    <div class="credit-row"><span>Kasper Lind</span><span>guitar solo, track 2</span></div>
    <div class="credit-row"><span>Ellis Fedder</span><span>beat programming, track 3</span></div>
    <div class="credit-row"><span>Oren Whitcombe (via Sessionfold)</span><span>piano, track 4</span></div>
    <div class="credit-row"><span>Tomasz Wilk (via Sessionfold)</span><span>vocals, track 4</span></div>
    <div class="credit-row"><span>Freya Olsson</span><span>violins, track 4</span></div>
    <div class="credit-row"><span>Mateo Ibarra Soler</span><span>cello, track 4</span></div>
    <div class="credit-row"><span>Kwame Asante (via Sessionfold)</span><span>drums, tracks 4, 5, 6, 7, 8, 9, 10</span></div>
    <div class="credit-row"><span>Hugo Brennan (via Sessionfold)</span><span>spoken word, tracks 5, 7, 10</span></div>
    <div class="credit-row"><span>Clara Whitfield</span><span>vocals, tracks 6 and 8</span></div>
    <div class="credit-row"><span>Marisol (via Sessionfold)</span><span>spoken word, track 7</span></div>
    <div class="credit-row"><span>Desmond Pike</span><span>vocals, tracks 7 and 10</span></div>
    <div class="credit-row"><span>Arlo Finch</span><span>vocals, track 9</span></div>
    <div class="credit-row"><span>Bram Okafor</span><span></span></div>
  </div>

  <p class="spaced-heading mastering-credit">Mastered by Gideon Shaw at HARBOUR ROOMS</p>

  <p class="thanks">Huge thanks to the team at Sessionfold, to all the amazing musicians who put their soul into this record, and to my family and friends who continue to inspire, support and encourage me in my music. Peace and love to the female and the male, the binary and the non-binary, the conformers and the non-conformers, the salt and the thunder.</p>

  <p class="signature">- rowan fedder, 2023<br><span class="website">lanternfield.com</span></p>
</main>
</body>
</html>
```